Maple Hollow Campground Billboard

We need an eye-catching, traffic-stopping design for a 15 ft x 10 ft billboard that will be located near the turn-off to our RV park in Colorado. Our park is located on the banks of the Rio Grande River and we want to emphasize that we have shady spots on the river. This is a link to our website www.maplehollowcampground.com and it will give you an idea about our park and what we have to offer. The billboard will be double-sided and face both directions of a busy highway. The park and the river is not visible from the highway, so we want to attract attention.

Target Market(s)

RV travelers on US Hwy 160 in South Fork, Colorado

Font styles to use
Sans Serif

Colors

Designer to choose colors to be used in the design.

Requirements
Must have
• Simple, eye-catching message.
Nice to have
• Incorporate our logo and give directions.
Should not have
• Too much information that can't be read while speeding down a busy highway.

```html
<!DOCTYPE html>
<html lang="en">
<head>
<meta charset="utf-8">
<title>Maple Hollow Campground Billboard</title>
<link rel="stylesheet" href="https://fonts.googleapis.com/css2?family=Alegreya:wght@700&family=Archivo:wght@800&display=swap">
<style>
  :root {
    --page: #e9e9e7;
    --forest: #1f3a24;
    --moss: #7b8c58;
    --bark: #84705e;
    --bark-dark: #6f5c4b;
    --cream: #f4efe4;
    --ink: #111111;
    --mist-light: #f2f2f2;
    --mist-mid: #d6d6d6;
    --mist-dark: #b3b3b3;
    --photo-top: #6f9fc4;
    --photo-bottom: #3f6d78;
  }
  html, body {
    margin: 0;
    width: 1200px;
    height: 1000px;
    overflow: hidden;
    background: var(--page);
  }
  .billboard {
    position: absolute;
    left: 0;
    top: 67px;
    width: 1200px;
    height: 866px;
    display: block;
  }
  .brand-name {
    font-family: "Alegreya", Georgia, serif;
    font-weight: 700;
    font-size: 66px;
    fill: var(--forest);
  }
  .amenities {
    font-family: "Alegreya", Georgia, serif;
    font-weight: 700;
    font-size: 28px;
    fill: var(--cream);
    letter-spacing: 0.5px;
  }
  .website {
    font-family: "Alegreya", Georgia, serif;
    font-weight: 700;
    font-size: 30px;
    fill: var(--bark-dark);
  }
  .phone {
    font-family: "Archivo", Arial, sans-serif;
    font-weight: 800;
    font-size: 64px;
    fill: var(--ink);
  }
</style>
</head>
<body>
<svg class="billboard" viewBox="0 0 1200 866" xmlns="http://www.w3.org/2000/svg">
  <defs>
    <linearGradient id="mist" x1="0" y1="0" x2="0" y2="1">
      <stop offset="0" stop-color="var(--mist-light)"/>
      <stop offset="0.6" stop-color="var(--mist-mid)"/>
      <stop offset="1" stop-color="var(--mist-dark)"/>
    </linearGradient>
    <linearGradient id="photoTone" x1="0" y1="0" x2="0" y2="1">
      <stop offset="0" stop-color="var(--photo-top)"/>
      <stop offset="1" stop-color="var(--photo-bottom)"/>
    </linearGradient>
    <clipPath id="panel"><rect width="1200" height="866"/></clipPath>
  </defs>

  <g clip-path="url(#panel)">
    <rect class="backdrop-photo" width="1200" height="866" fill="url(#mist)" role="img" aria-label="Faded black and white photo of a forested lakeshore"/>

    <rect class="band-rule" x="0" y="492" width="700" height="2" fill="var(--cream)"/>
    <rect class="amenities-band" x="0" y="500" width="700" height="155" fill="var(--bark)"/>
    <rect class="band-rule" x="0" y="661" width="700" height="2" fill="var(--bark)"/>

    <circle class="roundel-outer" cx="990" cy="436" r="410" fill="var(--bark)"/>
    <circle class="roundel-inner" cx="990" cy="436" r="396" fill="var(--moss)"/>
    <circle class="feature-photo" cx="990" cy="436" r="372" fill="url(#photoTone)" role="img" aria-label="Photo of a calm river pool ringed by pine trees and a rocky shore"/>
  </g>

  <text class="brand-name" x="313" y="215" text-anchor="middle">MAPLE HOLLOW</text>
  <text class="brand-name" x="313" y="295" text-anchor="middle">CAMPGROUND</text>

  <text class="amenities" x="310" y="551" text-anchor="middle">RV SPACES • RIVERFRONT SPACES</text>
  <text class="amenities" x="310" y="588" text-anchor="middle">TENT SITES • FISHING</text>
  <text class="amenities" x="310" y="625" text-anchor="middle">ON THE RIO GRANDE</text>

  <text class="website" x="313" y="722" text-anchor="middle">www.maplehollowcampground.com</text>
  <text class="phone" x="313" y="792" text-anchor="middle">800.555.0147</text>
</svg>
</body>
</html>
```